tolsa dead see mud mask label design

Hi
looking for a nice label design for dead see mud mask for tolsa beuty here is how other poepl are labeling it https://www.shopkarvio.com/TOP-Mineral-Clay-Face-Pack/dp/Q93RMZWLPK/ref=sr_1_1_a_it?ie=UTF8&qid=1582046917&sr=8-1&keywords=dead+see+mud+mask
we attached are logo and the label from the mfr we want the colors on the albel gray and purple

```html
<!DOCTYPE html>
<html lang="en">
<head>
<meta charset="utf-8">
<title>tolsa – Dead Sea Mud Mask Label</title>
<link rel="stylesheet" href="https://fonts.googleapis.com/css2?family=Bodoni+Moda:wght@500;700&family=Fira+Sans+Extra+Condensed:wght@300;400&display=swap">
<style>
  :root {
    --label-purple: #9a62d2;
    --ink-white: #ffffff;
    --ink-soft: #f4ecfb;
  }
  * { margin: 0; padding: 0; box-sizing: border-box; }
  html, body {
    width: 1200px;
    height: 900px;
    overflow: hidden;
    background: var(--label-purple);
  }
  .label {
    display: block;
    width: 1200px;
    height: 900px;
  }
  .label-ground { fill: var(--label-purple); }
  .title-rule { fill: var(--ink-white); }
  .brand-name {
    font-family: "Fira Sans Extra Condensed", sans-serif;
    font-weight: 400;
    font-size: 84px;
    fill: var(--ink-white);
  }
  .product-title {
    font-family: "Bodoni Moda", serif;
    font-weight: 500;
    font-size: 130px;
    fill: var(--ink-white);
  }
  .tagline {
    font-family: "Bodoni Moda", serif;
    font-weight: 700;
    font-size: 56px;
    fill: var(--ink-white);
  }
  .benefit,
  .net-weight {
    font-family: "Fira Sans Extra Condensed", sans-serif;
    font-weight: 300;
    font-size: 58px;
    fill: var(--ink-soft);
  }
</style>
</head>
<body>
  <svg class="label" viewBox="0 0 1200 900" xmlns="http://www.w3.org/2000/svg" role="img" aria-label="tolsa Dead Sea Mud Mask label">
    <rect class="label-ground" x="0" y="0" width="1200" height="900"/>

    <text class="brand-name" x="600" y="255" text-anchor="middle">tolsa</text>

    <rect class="title-rule" x="55" y="314" width="1090" height="4"/>
    <text class="product-title" x="60" y="437" textLength="1083" lengthAdjust="spacingAndGlyphs">DEAD SEA MUD MASK</text>
    <rect class="title-rule" x="55" y="461" width="1090" height="4"/>

    <text class="tagline" x="168" y="722" textLength="867" lengthAdjust="spacingAndGlyphs">Natural Mask from Dead Sea</text>
    <text class="benefit" x="260" y="786" textLength="680" lengthAdjust="spacingAndGlyphs">Deep Cleansing &amp; Purifying</text>
    <text class="net-weight" x="385" y="866" textLength="383" lengthAdjust="spacingAndGlyphs">8.8 fl.oz. | 250 g</text>
  </svg>
</body>
</html>
```